Business Card Design for The Brightwell Apparel House

Outlet Designer Clothing & Accessories Retailer

The Brightwell Apparel House is a high-end luxury outlet retailer. There is a wide selection of brands sold in the store that are from the most famous designer houses in Italy, France & Germany such

```html
<!DOCTYPE html>
<html lang="en">
<head>
<meta charset="utf-8">
<title>The Brightwell Apparel House – Business Card</title>
<link rel="stylesheet" href="https://fonts.googleapis.com/css2?family=Arimo:ital,wght@0,400;1,400&family=Questrial&display=swap">
<style>
  :root {
    --backdrop: #1d1d1d;
    --card: #ececec;
    --ink: #2a2a2a;
    --ink-soft: #555555;
    --placeholder: #dcdcdc;
  }
  html, body {
    margin: 0;
    padding: 0;
    width: 1200px;
    height: 931px;
    overflow: hidden;
    background: var(--backdrop);
  }
  .canvas {
    position: relative;
    width: 1200px;
    height: 931px;
  }
  .card {
    position: absolute;
    top: 203px;
    width: 524px;
    height: 524px;
    background: var(--card);
    color: var(--ink);
  }
  .card--front { left: 51px; }
  .card--back { left: 625px; }
  .frame {
    position: absolute;
    left: 94px;
    top: 28px;
    width: 337px;
    height: 365px;
    border: 2px solid var(--ink);
    box-sizing: border-box;
  }
  .holder {
    position: absolute;
    right: 18px;
    top: 22px;
    text-align: right;
    font-family: "Arimo", sans-serif;
  }
  .holder__name { font-size: 27px; line-height: 1.1; margin: 0; font-weight: 400; }
  .holder__role { font-size: 14px; color: var(--ink-soft); margin: 2px 0 0; }
  .contacts {
    position: absolute;
    right: 12px;
    top: 146px;
    margin: 0;
    padding: 0;
    list-style: none;
    font-family: "Arimo", sans-serif;
    font-size: 17px;
    text-align: right;
  }
  .contacts li { display: flex; align-items: center; justify-content: flex-end; gap: 10px; height: 23px; }
  .contacts svg { width: 13px; height: 15px; }
  .address {
    position: absolute;
    right: 18px;
    bottom: 14px;
    margin: 0;
    font-family: "Arimo", sans-serif;
    font-style: italic;
    font-size: 14.5px;
    line-height: 1.45;
    text-align: right;
  }
  .monogram-placeholder {
    position: absolute;
    inset: 0;
    background: var(--placeholder);
  }
  .wordmark {
    position: absolute;
    left: 0;
    right: 0;
    top: 412px;
    margin: 0;
    text-align: center;
    font-family: "Questrial", sans-serif;
    font-weight: 400;
    font-size: 31px;
    letter-spacing: 3px;
    line-height: 1.2;
    color: var(--ink);
    text-transform: uppercase;
  }
</style>
</head>
<body>
<main class="canvas">
  <section class="card card--front" aria-label="Card front">
    <div class="frame">
      <div class="holder">
        <p class="holder__name">Marcus Vell</p>
        <p class="holder__role">president</p>
      </div>
      <ul class="contacts">
        <li>(031) 557204.1186
          <svg viewBox="0 0 13 15" aria-hidden="true"><rect x="0.75" y="0.75" width="11.5" height="13.5" rx="2" fill="none" stroke="#2a2a2a" stroke-width="1.5"/><text x="6.5" y="11" font-size="10" text-anchor="middle" font-family="Arimo, sans-serif" fill="#2a2a2a">p</text></svg></li>
        <li>(031) 557204.409
          <svg viewBox="0 0 13 15" aria-hidden="true"><rect x="0.75" y="0.75" width="11.5" height="13.5" rx="2" fill="none" stroke="#2a2a2a" stroke-width="1.5"/><text x="6.5" y="11" font-size="10" text-anchor="middle" font-family="Arimo, sans-serif" fill="#2a2a2a">c</text></svg></li>
        <li>hello@brightwell.au
          <svg viewBox="0 0 13 15" aria-hidden="true"><rect x="0.75" y="0.75" width="11.5" height="13.5" rx="2" fill="none" stroke="#2a2a2a" stroke-width="1.5"/><text x="6.5" y="11" font-size="10" text-anchor="middle" font-family="Arimo, sans-serif" fill="#2a2a2a">e</text></svg></li>
      </ul>
      <p class="address">Linden Park Arcade<br>Harbour Lane Retail Suites<br>48 Harbour Lane Port Ellis Vic 3391</p>
    </div>
    <h1 class="wordmark">The Brightwell<br>Apparel House</h1>
  </section>

  <section class="card card--back" aria-label="Card back">
    <div class="frame">
      <div class="monogram-placeholder" role="img" aria-label="Spaced brand lettering arranged in a grid"></div>
    </div>
    <p class="wordmark">The Brightwell<br>Apparel House</p>
  </section>
</main>
</body>
</html>
```